Maple Lantern Business Card

Design of business cards

Target Market(s)

We are aiming as small business owners who need anything from basic business structures, website plans, business processes and quality assurance.

Industry/Entity Type

Business

Colors

Designer to choose colors to be used in the design.

Requirements
Nice to have
• I would prefer one side of the card to use the green from the logo. Prefer to have the same font as the logo.

```html
<!DOCTYPE html>
<html lang="en">
<head>
<meta charset="utf-8">
<title>Maple Lantern Business Card</title>
<link rel="stylesheet" href="https://fonts.googleapis.com/css2?family=Cinzel:wght@400;600&family=Open+Sans:wght@400&display=swap">
<style>
  :root {
    --leaf: #95bd33;
    --charcoal: #4a4a4c;
    --paper: #ffffff;
    --backdrop: #e6e6e6;
    --ink: #3a3a3a;
  }
  html, body {
    margin: 0;
    padding: 0;
    overflow: hidden;
  }
  .canvas {
    position: relative;
    width: 1200px;
    height: 795px;
    background: var(--backdrop);
    overflow: hidden;
  }
  .card {
    position: absolute;
    top: 250px;
    width: 520px;
    height: 297px;
    box-shadow: 0 3px 10px rgba(0,0,0,0.15);
    overflow: hidden;
  }
  .card--front { left: 50px; background: var(--paper); }
  .card--back { left: 630px; background: var(--leaf); }
  .wave { position: absolute; inset: 0; }

  .holder {
    position: absolute;
    right: 40px;
    top: 28px;
    text-align: right;
  }
  .holder__name {
    font-family: "Cinzel", serif;
    font-weight: 600;
    font-size: 22px;
    color: var(--leaf);
    letter-spacing: 1px;
    margin: 0;
  }
  .holder__role {
    font-family: "Open Sans", sans-serif;
    font-size: 11px;
    color: var(--ink);
    margin: 2px 0 0;
  }
  .contacts {
    position: absolute;
    left: 245px;
    top: 90px;
    margin: 0;
    padding: 0;
    list-style: none;
    font-family: "Open Sans", sans-serif;
    font-size: 11.5px;
    color: var(--ink);
  }
  .contacts li {
    display: flex;
    align-items: center;
    gap: 7px;
    height: 17px;
  }
  .contacts__icon {
    width: 11px;
    height: 11px;
    border-radius: 2px;
    background: var(--leaf);
    flex: none;
  }
  .brand {
    position: absolute;
    display: flex;
    align-items: center;
    gap: 10px;
    font-family: "Cinzel", serif;
    font-weight: 600;
  }
  .brand--front {
    left: 34px;
    top: 140px;
    font-size: 19px;
    color: var(--leaf);
  }
  .brand__dot {
    width: 14px;
    height: 14px;
    border-radius: 50%;
    background: currentColor;
    flex: none;
  }
  .brand--back {
    left: 110px;
    top: 104px;
    color: var(--paper);
    font-size: 26px;
    line-height: 1.15;
    letter-spacing: 2px;
    gap: 16px;
  }
  .brand--back .brand__dot { width: 22px; height: 22px; }
</style>
</head>
<body>
<div class="canvas">
  <section class="card card--front">
    <svg class="wave" width="520" height="297" viewBox="0 0 520 297">
      <path d="M122 297 C187 240 252 224 347 219 C440 214 502 162 520 102 L520 297 Z" fill="var(--leaf)"/>
      <path d="M95 297 C160 228 230 208 330 203 C430 198 492 145 520 78" fill="none" stroke="var(--charcoal)" stroke-width="5"/>
    </svg>
    <div class="holder">
      <h1 class="holder__name">Daniel Hart</h1>
      <p class="holder__role">Managing Director</p>
    </div>
    <ul class="contacts">
      <li><span class="contacts__icon"></span>00 004 512 7730</li>
      <li><span class="contacts__icon"></span>00 004 512 7730</li>
      <li><span class="contacts__icon"></span>00 004 512 7730</li>
      <li><span class="contacts__icon"></span>daniel.hart@mailbox.com.au</li>
      <li><span class="contacts__icon"></span>www.sitelink.com.au</li>
    </ul>
    <div class="brand brand--front"><span class="brand__dot"></span>Maple Lantern</div>
  </section>

  <section class="card card--back">
    <div class="brand brand--back">
      <span class="brand__dot"></span>
      <span>Maple<br>Lantern<br>Consulting</span>
    </div>
  </section>
</div>
</body>
</html>
```